Christmas and New Year wishes

I would like to send as a picture in a email a graphic that relates to:
-thanks for the collaboration / partnership in the past year (to be used for customers and partners)
-Wishes for Merry christmas and a successful 2019
-it should be colored and possibly include our logo color (www.velkarin.ch) (nice to have), or the name of our company

Target Market(s)

Customers and partners

Industry/Entity Type

It Company

Font styles to use
Sans Serif

Colors
9bcb3c
0455a3

Requirements
Must have
• Relation to christmas
• Relation to New year
Nice to have
• The colors below are near to the company logo color. But feel free to use any other logo
• a funny design
• Happy Customer or partner (supplier)
• Can be a mixture of text and drawing

```html
<!DOCTYPE html>
<html lang="en">
<head>
<meta charset="utf-8">
<title>Merry Christmas – Velkarin</title>
<link rel="stylesheet" href="https://fonts.googleapis.com/css2?family=Gochi+Hand&family=Lobster&display=swap">
<style>
  :root {
    --paper: #ffffff;
    --festive-red: #f2344f;
    --mint: #6cc3aa;
    --slate: #3f5f5c;
    --wordmark: #5c7c86;
    --pattern-red: rgba(242, 52, 79, 0.28);
    --pattern-mint: rgba(108, 195, 170, 0.32);
  }
  * { margin: 0; padding: 0; box-sizing: border-box; }
  html, body {
    width: 1200px;
    height: 1200px;
    overflow: hidden;
    background: var(--paper);
  }
  .greeting-card {
    position: relative;
    width: 1200px;
    height: 1200px;
    background: var(--paper);
    overflow: hidden;
  }
  .holiday-pattern {
    position: absolute;
    inset: 0;
    background:
      radial-gradient(ellipse 380px 440px at 50% 50%, var(--paper) 72%, rgba(255,255,255,0) 100%),
      linear-gradient(135deg, var(--pattern-red) 0%, var(--pattern-mint) 35%, var(--pattern-red) 65%, var(--pattern-mint) 100%);
  }
  .message {
    position: absolute;
    inset: 0;
    text-align: center;
  }
  .merry {
    position: absolute;
    top: 262px;
    width: 100%;
    font-family: "Gochi Hand", cursive;
    font-size: 62px;
    letter-spacing: 4px;
    color: var(--mint);
    line-height: 1;
  }
  .christmas {
    position: absolute;
    top: 330px;
    width: 100%;
    font-family: "Lobster", cursive;
    font-size: 104px;
    color: var(--festive-red);
    line-height: 1;
    letter-spacing: 2px;
  }
  .new-year {
    position: absolute;
    top: 440px;
    width: 100%;
    font-family: "Gochi Hand", cursive;
    font-size: 58px;
    color: var(--mint);
    line-height: 1;
  }
  .thanks {
    position: absolute;
    top: 560px;
    width: 100%;
    font-family: "Gochi Hand", cursive;
    font-size: 62px;
    color: var(--festive-red);
    line-height: 78px;
  }
  .wordmark {
    position: absolute;
    top: 860px;
    width: 100%;
    font-family: "Gochi Hand", cursive;
    font-size: 60px;
    letter-spacing: 3px;
    color: var(--wordmark);
    line-height: 1;
  }
</style>
</head>
<body>
  <main class="greeting-card">
    <div class="holiday-pattern" role="img" aria-label="Border of scattered Christmas illustrations: snowflakes, gifts, bells, candy canes, holly, trees, hearts and music notes in red and mint"></div>
    <section class="message">
      <p class="merry">MERRY</p>
      <h1 class="christmas">Christmas</h1>
      <p class="new-year">and a happy new year</p>
      <p class="thanks">Thanks for the<br>collaboration in the<br>past year</p>
      <p class="wordmark">velkarin</p>
    </section>
  </main>
</body>
</html>
```